Stationary for an International Church

We need a design for various stationery items - letters/envelopes, Word/PowerPoint pages, based on
- the LHF Logo
- the primary color "bright turquoise" ("vivid cyan"), hex #08e8de
- the font family: Frutiger 55 Roman
To get an image of our organization, please visit lanternhill.org, recent blog entries at https://www.lanternhill.org/blog or annual reports at Downloads

Target Market(s)

Congregation and business partners of the Chruch

Font styles to use
Other font styles liked:
• requirement: Frutiger 55 Roman

Colors
33b8a4

Requirements
Must have
• simple, modern design, a bit unique

```html
<!DOCTYPE html>
<html lang="en">
<head>
<meta charset="utf-8">
<title>Lantern Hill Fellowship – Stationery</title>
<link href="https://fonts.googleapis.com/css2?family=Hind:wght@400;500;600&family=Arimo:wght@400&display=swap" rel="stylesheet">
<style>
  :root {
    --backdrop: #abaaab;
    --paper: #ffffff;
    --brand: #5ec7c9;
    --brand-faint: #e5f5f5;
    --ink: #3a3a3a;
    --body-ink: #555555;
  }
  * { box-sizing: border-box; margin: 0; padding: 0; }
  html, body { width: 1200px; height: 770px; overflow: hidden; }
  body { background: var(--backdrop); position: relative; font-family: "Hind", sans-serif; color: var(--ink); }

  .sheet { position: absolute; background: var(--paper); box-shadow: 0 1px 3px rgba(0,0,0,.3); overflow: hidden; }

  /* Letterhead */
  .letterhead { left: 94px; top: 63px; width: 456px; height: 643px; }
  .faint-mark { position: absolute; border-radius: 50%; background: var(--brand-faint); }
  .letterhead .faint-mark { left: 170px; top: 250px; width: 300px; height: 300px; }

  .lockup { position: absolute; width: 84px; text-align: center; color: var(--brand); }
  .lockup .mark-dot { display: block; width: 22px; height: 22px; border-radius: 50%; background: var(--brand); margin: 0 auto 8px; }
  .lockup .name { font-size: 5.8px; font-weight: 500; letter-spacing: .45px; line-height: 1.3; text-transform: uppercase; white-space: nowrap; }
  .lockup .rule { height: 1px; background: var(--brand); margin: 3px 0 5px; }
  .lockup .tagline { font-size: 5.5px; letter-spacing: .5px; white-space: nowrap; }
  .letterhead .lockup { left: 43px; top: 77px; }

  .address { position: absolute; font-size: 8px; line-height: 9.8px; color: var(--ink); }
  .address .org { color: var(--brand); font-weight: 600; }
  .letterhead .address { left: 331px; top: 91px; }

  .letter { position: absolute; left: 47px; top: 245px; width: 360px; font-family: "Arimo", sans-serif; color: var(--body-ink); }
  .letter .salutation { font-size: 9.6px; color: var(--ink); margin-bottom: 10px; }
  .letter p { font-size: 6.7px; line-height: 10.8px; text-align: justify; margin-bottom: 10.8px; }
  .letter .closing { margin-top: 32px; }
  .signature-area { display: block; width: 58px; height: 18px; margin-top: 14px; background: var(--brand-faint); }

  .contact-row { position: absolute; left: 47px; top: 589px; width: 360px; height: 30px; font-size: 7.6px; color: var(--ink); }
  .contact { position: absolute; top: 0; }
  .contact svg { display: block; width: 11px; height: 11px; margin-bottom: 5px; }
  .contact.phone { left: 0; }
  .contact.phone svg { margin-left: 21px; }
  .contact.fax { left: 143px; }
  .contact.fax svg { margin-left: 25px; }
  .contact.web { right: 0; text-align: right; }
  .contact.web svg { margin-left: 30px; }

  /* Envelope back */
  .envelope-back { left: 644px; top: 331px; width: 508px; height: 251px; }
  .flap { position: absolute; left: 0; top: 0; width: 508px; height: 82px; }
  .flap-name { position: absolute; left: 0; top: 28px; width: 508px; text-align: center; color: var(--paper); font-size: 13px; font-weight: 600; letter-spacing: 1.5px; }

  /* Envelope front */
  .envelope-front { left: 584px; top: 455px; width: 509px; height: 251px; }
  .envelope-front .faint-mark { left: 390px; top: 40px; width: 160px; height: 160px; }
  .envelope-front .lockup { left: 25px; top: 56px; }
  .envelope-front .address { left: 29px; top: 116px; }
</style>
</head>
<body>

  <section class="sheet letterhead">
    <div class="faint-mark" aria-hidden="true"></div>

    <div class="lockup">
      <span class="mark-dot"></span>
      <div class="name">Lantern Hill Fellowship</div>
      <div class="rule"></div>
      <div class="tagline">Light for every path</div>
    </div>

    <div class="address">
      <div class="org">Lantern Hill Fellowship</div>
      <div>2-14-3 Kitayama,</div>
      <div>Minato-ku</div>
      <div>Tokyo 108-0072</div>
    </div>

    <article class="letter">
      <div class="salutation">Dear Mr. Harlow,</div>
      <p>Lorem ipsum dolor sit amet, consectetur adipiscing elit. Donec orci purus, luctus vitae dignissim eu, iaculis sed purus. Vivamus faucibus, ipsum nec aliquet viverra, leo mauris condimentum ligula, sit amet sagittis enim ligula quis arcu. Nam egestas tortor id nisi porttitor mattis. In tortor ante, ultricies in suscipit a, tempus non massa. Vivamus et auctor mi. Fusce vel massa nulla. Phasellus nec eros mauris, et scelerisque orci.</p>
      <p>Donec malesuada orci vitae nulla accumsan porta a id massa. Quisque accumsan iaculis magna sit amet fringilla. Maecenas consequat, magna eget tincidunt semper, odio nibh rutrum mi, id feugiat ante nisi eu risus. Vestibulum nunc orci, rhoncus a placerat in, ultricies in mi. Cras mattis varius eros, vel fringilla nisi suscipit eget. Quisque scelerisque sagittis nulla at porttitor.</p>
      <p>Sed id augue vitae urna euismod commodo aliquet a quam. Pellentesque arcu velit, cursus et malesuada ut, consequat et diam. Nullam erat sem, rhoncus id ullamcorper vitae, rhoncus et arcu. In ultricies ultricies nulla, ut rutrum nisi iaculis at. Donec eu magna a metus ornare faucibus. Fusce aliquet faucibus ultricies. Morbi semper, est id tincidunt gravida, sem arcu adipiscing lacus, ac bibendum nulla leo eu purus. Quisque nec diam sed risus consectetur accumsan quis quis nibh. Vestibulum id purus lorem.</p>
      <p class="closing">Sincerely,</p>
      <span class="signature-area" role="img" aria-label="Handwritten signature"></span>
    </article>

    <div class="contact-row">
      <div class="contact phone">
        <svg viewBox="0 0 12 12" aria-hidden="true"><circle cx="6" cy="6" r="6" fill="var(--brand)"/><path d="M4 3.2c.4-.3.7 0 .9.4l.3.7c.1.3 0 .5-.2.7l-.3.3c.3.7.8 1.2 1.5 1.5l.3-.3c.2-.2.4-.3.7-.2l.7.3c.4.2.7.5.4.9-.4.6-1 .9-1.6.7C5.3 7.7 4.3 6.7 3.8 5.3c-.2-.7.1-1.4.2-2.1z" fill="#fff"/></svg>
        (03) 5210-3318
      </div>
      <div class="contact fax">
        <svg viewBox="0 0 12 12" aria-hidden="true"><circle cx="6" cy="6" r="6" fill="var(--brand)"/><rect x="4" y="2.8" width="4" height="2" fill="#fff"/><rect x="3" y="5" width="6" height="2.6" rx=".4" fill="#fff"/><rect x="4" y="7.2" width="4" height="2" fill="#fff"/></svg>
        (050) 6120-4471
      </div>
      <div class="contact web">
        <svg viewBox="0 0 12 12" aria-hidden="true"><circle cx="6" cy="6" r="6" fill="var(--brand)"/><g fill="none" stroke="#fff" stroke-width=".7"><circle cx="6" cy="6" r="3.3"/><ellipse cx="6" cy="6" rx="1.4" ry="3.3"/><path d="M2.7 6h6.6"/></g></svg>
        www.lanternhill.org
      </div>
    </div>
  </section>

  <section class="sheet envelope-back">
    <svg class="flap" viewBox="0 0 508 82" aria-hidden="true">
      <path d="M0 0 H508 L496 40 Q487 82 450 82 H58 Q21 82 12 40 Z" fill="var(--brand)"/>
    </svg>
    <div class="flap-name">LHF</div>
  </section>

  <section class="sheet envelope-front">
    <div class="faint-mark" aria-hidden="true"></div>
    <div class="lockup">
      <span class="mark-dot"></span>
      <div class="name">Lantern Hill Fellowship</div>
      <div class="rule"></div>
      <div class="tagline">Light for every path</div>
    </div>
    <div class="address">
      <div class="org">Lantern Hill Fellowship</div>
      <div>2-14-3 Kitayama, Minato-ku</div>
      <div>Tokyo 108-0072</div>
    </div>
  </section>

</body>
</html>
```